Einladungskarten für Firmenjubiläum
Zielgruppe
Ich brauche eine digitale Einladungskarte zum 10-jährigen Firmenjubiläum, das am 12. Juli stattfinden soll. Zu uns; wir sind ein Ingenieurbüro im Bereich Digitalisierung und sicherheitskritische Systeme, wie sie in Flugzeugen, medizinischen Geräten, modernen Autos etc. vorkommen. Autonomes Fahren und Raumfahrtmedizin, sowie Fahrzeugsicherheit und Cyber-Sicherheit gehören z. B. zu unseren Schwerpunktthemen.
Aufgabenstellung
Ich bin für Ideen offen, die sich an dem Inhalt unserer Website anlehnen.

```html
<!DOCTYPE html>
<html lang="de">
<head>
<meta charset="utf-8">
<title>Einladung – 10 jähriges Firmenjubiläum</title>
<link rel="stylesheet" href="https://fonts.googleapis.com/css2?family=Titillium+Web:wght@400;600;700&display=swap">
<style>
  :root {
    --brand-blue: #1e96d6;
    --brand-grey: #777779;
    --text-grey: #6e6e70;
    --ink: #000000;
    --paper: #ffffff;
  }
  html, body {
    margin: 0;
    padding: 0;
    overflow: hidden;
    background: var(--paper);
  }
  .card {
    position: relative;
    width: 848px;
    height: 1200px;
    overflow: hidden;
    background: var(--paper);
    font-family: "Titillium Web", sans-serif;
    color: var(--text-grey);
  }
  .decor {
    position: absolute;
    inset: 0;
    width: 848px;
    height: 1200px;
  }
  .brand-bar {
    position: absolute;
    left: 0;
    top: 40px;
    width: 255px;
    height: 72px;
    background: var(--ink);
    display: flex;
    align-items: center;
    justify-content: center;
  }
  .brand-name {
    color: var(--paper);
    font-weight: 600;
    font-size: 19px;
    letter-spacing: 1.5px;
  }
  .hero-photo {
    position: absolute;
    left: 85px;
    top: 150px;
    width: 447px;
    height: 481px;
    clip-path: polygon(50% 0%, 100% habitat, 100% 74.8%, 50% 100%, 0% 74.8%, 0% 24.7%);
    clip-path: polygon(50% 0%, 100% 24.7%, 100% 74.8%, 50% 100%, 0% 74.8%, 0% 24.7%);
    background: linear-gradient(150deg, #efe6da 0%, #b9aca6 35%, #4d4a5a 65%, #2a2a3c 100%);
  }
  .jubilee-title {
    position: absolute;
    left: 500px;
    top: 575px;
    margin: 0;
    color: var(--brand-blue);
    font-weight: 600;
    font-size: 44px;
    line-height: 46px;
  }
  .event-box {
    position: absolute;
    left: 64px;
    top: 803px;
    width: 718px;
    height: 146px;
    border: 3px solid var(--brand-blue);
    border-radius: 76px;
  }
  .event-date {
    position: absolute;
    left: 190px;
    top: 853px;
    width: 195px;
    text-align: center;
    font-size: 34px;
    font-weight: 600;
    line-height: 40px;
    letter-spacing: 0.5px;
  }
  .event-divider {
    position: absolute;
    left: 417px;
    top: 818px;
    width: 3px;
    height: 121px;
    background: var(--brand-blue);
  }
  .event-address {
    position: absolute;
    left: 500px;
    top: 826px;
    width: 252px;
    margin: 0;
    text-align: center;
    font-style: normal;
    font-size: 20px;
    line-height: 34px;
  }
  .invitation-line {
    position: absolute;
    left: 0;
    top: 982px;
    width: 848px;
    margin: 0;
    text-align: center;
    font-size: 24px;
    font-weight: 600;
    line-height: 31px;
    color: var(--text-grey);
  }
</style>
</head>
<body>
<main class="card">
  <svg class="decor" viewBox="0 0 848 1200" aria-hidden="true">
    <g fill="none" stroke-width="6" stroke-linejoin="miter">
      <!-- top right hexagon pair -->
      <polygon stroke="var(--brand-blue)" points="734,41 803,77 803,151 734,187 665,151 665,77"/>
      <polygon stroke="var(--brand-grey)" points="781,41 827,65 827,115 781,139 735,115 735,65"/>
      <!-- left edge hexagon pair -->
      <polygon stroke="var(--brand-grey)" points="-5,452 42,481 42,541 -5,570 -52,541 -52,481"/>
      <polygon stroke="var(--brand-blue)" points="0,489 68,524 68,600 0,635 -68,600 -68,524"/>
      <!-- bottom right hexagon pair -->
      <polygon stroke="var(--brand-grey)" points="828,1059 867,1082 867,1128 828,1150 789,1128 789,1082"/>
      <polygon stroke="var(--brand-blue)" points="850,1089 894,1111 894,1155 850,1178 806,1155 806,1111"/>
    </g>
  </svg>

  <div class="brand-bar">
    <span class="brand-name">NOVARIS Technologies GmbH</span>
  </div>

  <div class="hero-photo" role="img" aria-label="Foto: Kolleginnen und Kollegen stoßen in einem hellen Büro mit Sektgläsern an"></div>

  <svg class="decor" viewBox="0 0 848 1200" aria-hidden="true">
    <!-- anniversary number badge -->
    <polygon fill="var(--paper)" stroke="var(--brand-blue)" stroke-width="6" points="428,534 489,568 489,631 428,665 367,631 367,568"/>
    <text x="429" y="622" text-anchor="middle" fill="var(--brand-blue)" font-family="Titillium Web, sans-serif" font-weight="600" font-size="58">10</text>

    <!-- calendar icon -->
    <g class="icon-calendar">
      <rect x="81" y="840" width="86" height="76" rx="4" fill="var(--brand-blue)"/>
      <g fill="var(--paper)">
        <rect x="89" y="862" width="16" height="12"/>
        <rect x="108" y="862" width="16" height="12"/>
        <rect x="127" y="862" width="16" height="12"/>
        <rect x="146" y="862" width="13" height="12"/>
        <rect x="89" y="877" width="16" height="12"/>
        <rect x="108" y="877" width="16" height="12"/>
        <rect x="127" y="877" width="16" height="12"/>
        <rect x="146" y="877" width="13" height="12"/>
        <rect x="89" y="892" width="16" height="14"/>
        <rect x="108" y="892" width="16" height="14"/>
        <rect x="127" y="892" width="16" height="14"/>
        <rect x="146" y="892" width="13" height="14"/>
      </g>
      <rect x="94" y="830" width="12" height="24" rx="6" fill="var(--brand-blue)" stroke="var(--paper)" stroke-width="2.5"/>
      <rect x="142" y="830" width="12" height="24" rx="6" fill="var(--brand-blue)" stroke="var(--paper)" stroke-width="2.5"/>
    </g>

    <!-- location pin icon -->
    <g class="icon-pin" fill="none" stroke="var(--brand-blue)" stroke-width="3.5">
      <path d="M467,908 C455,888 446,875 446,862 A21,21 0 0 1 488,862 C488,875 479,888 467,908 Z"/>
      <circle cx="467" cy="861" r="10"/>
      <ellipse cx="467" cy="912" rx="12" ry="4"/>
    </g>
  </svg>

  <h1 class="jubilee-title">jähriges<br>Firmenjubiläum</h1>

  <section class="event-box" aria-label="Termin und Ort"></section>
  <div class="event-date">12.07.2024</div>
  <div class="event-divider"></div>
  <address class="event-address">
    Novaris Technologies GmbH<br>
    Lindenhofer Weg 8<br>
    24117 Kiel
  </address>

  <p class="invitation-line">
    Ihre persönliche Einladung zum 10. Jährigen Firmenjubiläum<br>
    der Novaris Technologies GmbH
  </p>
</main>
</body>
</html>
```